Quotation (Proposal) Form

We are looking for a redesign of an existing form - one that fits our new marketing material better and, frankly, a form that looks a lot nicer than the boring form we use today. 8.5"x11". CMYK. Minimum 300 dpi necessary for printing. I have attached our current quote form as well as some other designs that show the direction we are going in. Please note, that this has to be able to have our people manually write in pen on it when we provide it to potential customers. Thank you!

Target Market(s)

Residential homeowners

Industry/Entity Type

Snow Removal

Font styles to use
Sans Serif

Colors

Designer to choose colors to be used in the design.

Requirements
Must have
• Should be easy to read and look great. Should also add the following text - "Exclusively serving Northeast Grand Rapids and suburbs"
Nice to have
• Similar concept to other marketing material we have done (attached). Easy to read. Professional.
Should not have
• Cluttered look. Unevenly spaced.

```html
<!DOCTYPE html>
<html lang="en">
<head>
<meta charset="utf-8">
<title>Birch Hollow Landscaping – Snowplowing Seasonal Quote</title>
<link href="https://fonts.googleapis.com/css2?family=Lato:ital,wght@0,400;0,700;0,900;1,700&family=Exo+2:wght@800&display=swap" rel="stylesheet">
<style>
  :root{
    --ink:#1b1b1b;
    --black:#111111;
    --green:#3dba5f;
    --green-dark:#2e9c4c;
    --blue:#5b9fd8;
    --white:#ffffff;
    --gold:#d8b43a;
    --badge-green:#2f9e6a;
    --photo-a:#dfe5ea;
    --photo-b:#8a949c;
  }
  *{box-sizing:border-box;margin:0;padding:0}
  html,body{width:960px;height:1200px;overflow:hidden;background:var(--white)}
  body{font-family:"Lato",sans-serif;color:var(--ink);position:relative}
  .sheet{position:absolute;inset:0;width:960px;height:1200px}
  .header-bg{position:absolute;left:0;top:0}
  .frame{position:absolute;left:0;top:0}

  .brand{position:absolute;left:50px;top:78px;color:var(--white);font-weight:400;font-size:33px;letter-spacing:.2em;line-height:1.15;text-transform:uppercase}
  .brand span{display:block;font-size:14px;letter-spacing:.62em;margin-top:8px;padding-left:56px}
  .contact{position:absolute;left:48px;top:164px;color:var(--white);font-size:19px;line-height:25px}

  .client-box{position:absolute;left:468px;top:40px;width:464px;height:184px;background:var(--white);border-radius:30px 40px 0 40px;border-radius:0 40px 0 40px;border-top-left-radius:30px;padding:16px 24px 0 28px}
  .field{display:flex;align-items:flex-end;font-size:17px;height:31px;gap:6px}
  .field .line{flex:1;border-bottom:1.5px solid var(--ink);height:1px;margin-bottom:5px}
  .field .short{flex:0 0 84px}
  .field .gap{width:14px}

  .badges{position:absolute;left:527px;top:260px;display:flex;gap:22px;align-items:center}
  .badge{width:56px;height:70px}

  .photo{position:absolute;border-radius:50%;border:3px solid var(--green);background:radial-gradient(circle at 45% 40%,var(--photo-a),var(--photo-b));box-shadow:0 0 0 5px var(--white)}
  .photo-one{left:112px;top:300px;width:160px;height:160px}
  .photo-two{left:290px;top:255px;width:190px;height:190px}

  .service-tab{position:absolute;left:489px;top:364px;width:422px;height:80px;background:var(--black);border-radius:26px 26px 0 26px;color:var(--green);font-family:"Exo 2",sans-serif;font-weight:800;font-size:49px;letter-spacing:.01em;display:flex;align-items:center;justify-content:center}

  .quote-title{position:absolute;left:112px;top:470px;color:var(--green);font-weight:700;font-size:29px}
  .features{position:absolute;left:112px;top:511px;list-style:none;width:770px}
  .features li{display:flex;gap:12px;font-size:20.5px;line-height:26px;margin-bottom:6.5px}
  .features svg{flex:0 0 18px;margin-top:5px}

  .payments{position:absolute;left:180px;top:956px;width:670px}
  .pay-row{display:flex;justify-content:flex-end;align-items:center;height:31px;font-style:italic;font-weight:700;font-size:17.5px}
  .pay-row .amount{width:160px;height:31px;margin-left:14px;border:2px solid var(--green);border-radius:0 26px 0 26px;font-style:normal;font-size:18px;padding-left:26px;display:flex;align-items:center}

  .sign-box{position:absolute;left:165px;top:1041px;width:630px;height:132px;background:var(--white);border:4px solid var(--green);border-radius:0 30px 0 30px;padding:14px 60px 0 60px}
  .sign-box h2{font-weight:400;font-size:21px;text-align:center;margin-bottom:8px}
  .sign-row{display:flex;align-items:flex-end;font-size:17px;height:33px;gap:10px}
  .sign-row .line{border-bottom:1.5px solid var(--ink);margin-bottom:5px}
  .sign-row .long{flex:1}
  .sign-row .date{width:122px}
  .sign-row .date-label{margin-left:6px}
</style>
</head>
<body>
<main class="sheet">
  <svg class="header-bg" width="960" height="420" viewBox="0 0 960 420" aria-hidden="true">
    <path d="M0 300 C150 270 340 325 500 312 C660 300 800 312 960 345 V0 H0 Z" fill="var(--blue)"/>
    <path d="M0 286 C150 256 340 311 500 298 C660 286 800 298 960 330 V0 H0 Z" fill="var(--black)"/>
  </svg>

  <svg class="frame" width="960" height="1200" viewBox="0 0 960 1200" aria-hidden="true">
    <rect x="56" y="405" width="850" height="672" rx="46" fill="none" stroke="var(--green)" stroke-width="4"/>
    <rect x="72" y="420" width="818" height="644" rx="32" fill="none" stroke="var(--green)" stroke-width="3"/>
  </svg>

  <div class="brand">Birch Hollow<span>Landscaping</span></div>
  <address class="contact" style="font-style:normal">
    1840 Larkspur Valley Road NE<br>
    Grand Rapids, MI 49546<br>
    Ph: (555) 214-7730<br>
    Email: office@birchhollow.com
  </address>

  <section class="client-box" aria-label="Customer details">
    <div class="field">Name <span class="line"></span></div>
    <div class="field">Address <span class="line"></span></div>
    <div class="field">Phone <span class="line"></span></div>
    <div class="field">City <span class="line"></span><span class="gap"></span>Zip <span class="line short"></span></div>
    <div class="field">Email Address <span class="line"></span></div>
  </section>

  <div class="badges" aria-label="Service awards">
    <svg class="badge" viewBox="0 0 56 70"><path d="M4 4 H52 V48 L28 66 L4 48 Z" fill="var(--gold)"/></svg>
    <svg class="badge" viewBox="0 0 56 70"><path d="M16 46 L10 66 L20 60 L26 68 L28 50 Z M40 46 L46 66 L36 60 L30 68 L28 50 Z" fill="var(--badge-green)"/><circle cx="28" cy="28" r="25" fill="var(--gold)"/></svg>
    <svg class="badge" viewBox="0 0 56 70" style="width:70px"><path d="M4 6 H52 V42 C52 56 40 62 28 66 C16 62 4 56 4 42 Z" fill="var(--gold)" transform="scale(1.25 1)"/></svg>
    <svg class="badge" viewBox="0 0 56 70" style="width:70px"><path d="M5 10 C20 2 36 2 51 10 V40 C51 56 40 62 28 66 C16 62 5 56 5 40 Z" fill="var(--badge-green)" stroke="var(--white)" stroke-width="2" transform="scale(1.2 1)"/></svg>
  </div>

  <div class="photo photo-one" role="img" aria-label="Photo of a pickup truck with a snowplow clearing snow at night"></div>
  <div class="photo photo-two" role="img" aria-label="Photo of a white truck with a yellow plow blade pushing snow"></div>

  <div class="service-tab">SNOWPLOWING</div>

  <h1 class="quote-title">Unlimited Plowing Seasonal Quote</h1>

  <ul class="features">
    <li><svg width="18" height="18" viewBox="0 0 18 18"><circle cx="9" cy="9" r="7.5" fill="none" stroke="var(--green)" stroke-width="1.6"/><path d="M5.5 9.2 L8.2 11.8 L16 4" fill="none" stroke="var(--green)" stroke-width="1.8"/></svg><span>Plowing will be done when snow has accumulated 1” or more, normally by 6am, depending upon time and amount</span></li>
    <li><svg width="18" height="18" viewBox="0 0 18 18"><circle cx="9" cy="9" r="7.5" fill="none" stroke="var(--green)" stroke-width="1.6"/><path d="M5.5 9.2 L8.2 11.8 L16 4" fill="none" stroke="var(--green)" stroke-width="1.8"/></svg><span>We return to clean your driveway approach after your street has been plowed</span></li>
    <li><svg width="18" height="18" viewBox="0 0 18 18"><circle cx="9" cy="9" r="7.5" fill="none" stroke="var(--green)" stroke-width="1.6"/><path d="M5.5 9.2 L8.2 11.8 L16 4" fill="none" stroke="var(--green)" stroke-width="1.8"/></svg><span>Plowing multiple times per 24 hour period during heavy snowfalls</span></li>
    <li><svg width="18" height="18" viewBox="0 0 18 18"><circle cx="9" cy="9" r="7.5" fill="none" stroke="var(--green)" stroke-width="1.6"/><path d="M5.5 9.2 L8.2 11.8 L16 4" fill="none" stroke="var(--green)" stroke-width="1.8"/></svg><span>A fleet of 20 plow trucks with multiple backup plow trucks to ensure<br>our performance</span></li>
    <li><svg width="18" height="18" viewBox="0 0 18 18"><circle cx="9" cy="9" r="7.5" fill="none" stroke="var(--green)" stroke-width="1.6"/><path d="M5.5 9.2 L8.2 11.8 L16 4" fill="none" stroke="var(--green)" stroke-width="1.8"/></svg><span>Email based plowing information with real time updates for clients</span></li>
    <li><svg width="18" height="18" viewBox="0 0 18 18"><circle cx="9" cy="9" r="7.5" fill="none" stroke="var(--green)" stroke-width="1.6"/><path d="M5.5 9.2 L8.2 11.8 L16 4" fill="none" stroke="var(--green)" stroke-width="1.8"/></svg><span>Hard rubber plow edges protect concrete and pavement from<br>scratches and rust marks</span></li>
    <li><svg width="18" height="18" viewBox="0 0 18 18"><circle cx="9" cy="9" r="7.5" fill="none" stroke="var(--green)" stroke-width="1.6"/><path d="M5.5 9.2 L8.2 11.8 L16 4" fill="none" stroke="var(--green)" stroke-width="1.8"/></svg><span>Hand shoveling of front walkways and porches available</span></li>
    <li><svg width="18" height="18" viewBox="0 0 18 18"><circle cx="9" cy="9" r="7.5" fill="none" stroke="var(--green)" stroke-width="1.6"/><path d="M5.5 9.2 L8.2 11.8 L16 4" fill="none" stroke="var(--green)" stroke-width="1.8"/></svg><span>Salting of driveways available</span></li>
    <li><svg width="18" height="18" viewBox="0 0 18 18"><circle cx="9" cy="9" r="7.5" fill="none" stroke="var(--green)" stroke-width="1.6"/><path d="M5.5 9.2 L8.2 11.8 L16 4" fill="none" stroke="var(--green)" stroke-width="1.8"/></svg><span>Fully licensed and insured for your protection</span></li>
    <li><svg width="18" height="18" viewBox="0 0 18 18"><circle cx="9" cy="9" r="7.5" fill="none" stroke="var(--green)" stroke-width="1.6"/><path d="M5.5 9.2 L8.2 11.8 L16 4" fill="none" stroke="var(--green)" stroke-width="1.8"/></svg><span>A slip free surface can’t be guaranteed</span></li>
    <li><svg width="18" height="18" viewBox="0 0 18 18"><circle cx="9" cy="9" r="7.5" fill="none" stroke="var(--green)" stroke-width="1.6"/><path d="M5.5 9.2 L8.2 11.8 L16 4" fill="none" stroke="var(--green)" stroke-width="1.8"/></svg><span>Exclusively servicing Northeast Grand Rapids and suburbs</span></li>
  </ul>

  <section class="payments" aria-label="Payment options">
    <div class="pay-row">One payment due by October 31 <span class="amount">$</span></div>
    <div class="pay-row">Two equal installments due by October 31 &amp; December 31 <span class="amount">$</span></div>
  </section>

  <section class="sign-box" aria-label="Signatures">
    <h2>Please Sign And Return Copy With Payment</h2>
    <div class="sign-row">Birch Hollow <span class="line long"></span><span class="date-label">Date</span><span class="line date"></span></div>
    <div class="sign-row">Customer <span class="line long"></span><span class="date-label">Date</span><span class="line date"></span></div>
  </section>
</main>
</body>
</html>
```